Training flyer for 1/2 day modules

We need a flyer to be designed for some training sessions. It needs to be professional for the defence industry. It also needs to be able to be completed online - with tick boxes etc. Should be A4 back to back. Included in the documents below is some samples of previous brochures that we have had. Also below are some reviews from previous training - please use these somewhere;

- Great training, best I've ever had on this topic.
- Great presenter - very knowledgable.
- Course was very well presented and organised.

PLEASE USE MODULE TRAINING MOCK-UP FLYER ATTACHED FILE FOR CONTENT.

Target Market(s)

Defence industry

Industry/Entity Type

Defence

Requirements
Must have
• professional look - be able to be completed online,

```html
<!DOCTYPE html>
<html lang="en">
<head>
<meta charset="utf-8">
<title>Module Training Flyer</title>
<link href="https://fonts.googleapis.com/css2?family=Oswald:wght@500;700&family=Open+Sans:ital,wght@0,400;0,600;0,700;1,400&display=swap" rel="stylesheet">
<style>
  :root{
    --navy:#0c2b47;
    --navy-deep:#071c30;
    --green:#5aa832;
    --green-dark:#3f8a22;
    --blue:#1d74bb;
    --ink:#333b44;
    --paper:#ffffff;
    --row:#eef3f7;
    --line:#c9d3dc;
  }
  *{margin:0;padding:0;box-sizing:border-box}
  html,body{width:900px;height:1200px;overflow:hidden;background:var(--paper)}
  body{font-family:"Open Sans",Arial,sans-serif;color:var(--ink);position:relative}

  .hero-photo{position:absolute;left:0;top:0;width:440px;height:360px;
    background:linear-gradient(160deg,#3d6f93 0%,#1b4569 45%,var(--navy) 100%);
    clip-path:polygon(0 0,100% 0,78% 100%,0 100%)}
  .hero-band{position:absolute;left:0;top:0;width:900px;height:360px}

  .brand{position:absolute;left:520px;top:44px;display:flex;align-items:center;gap:14px}
  .brand-dot{width:56px;height:56px;border-radius:50%;background:var(--green);flex:none}
  .brand-name{font-weight:700;font-size:24px;color:var(--navy);line-height:1.15;width:240px}

  .title{position:absolute;left:40px;top:380px;width:390px}
  .title h1{font-family:"Oswald",sans-serif;font-weight:700;font-size:84px;line-height:.95;color:var(--blue);text-transform:uppercase}
  .title h1 .accent{color:var(--green)}
  .subtitle{margin-top:14px;background:var(--green);color:#fff;font-family:"Oswald",sans-serif;font-weight:500;font-size:22px;letter-spacing:1px;padding:6px 12px;text-transform:uppercase}

  .sessions{position:absolute;left:40px;top:598px;width:390px;border-collapse:collapse;font-size:13px}
  .sessions td{padding:7px 10px;font-weight:600;text-transform:uppercase;vertical-align:middle}
  .sessions tr:nth-child(odd) td{background:var(--row)}
  .sessions td.city{color:var(--navy)}
  .sessions td.date{text-align:right;color:var(--green-dark)}
  .sessions td.pick{width:30px;padding-right:0}

  .tick{appearance:none;-webkit-appearance:none;width:16px;height:16px;border:2px solid var(--green);border-radius:3px;background:#fff;vertical-align:middle;flex:none}
  .tick:checked{background:var(--green)}

  .price{position:absolute;left:40px;top:728px;font-family:"Oswald",sans-serif;font-weight:700;font-size:40px;color:var(--blue)}
  .price small{font-size:24px;color:var(--green)}

  .team-photo{position:absolute;left:0;top:800px;width:450px;height:260px;
    background:linear-gradient(180deg,#dfe6ec 0%,#9fb1c0 60%,#5c7489 100%)}

  .modules{position:absolute;left:480px;top:150px;width:390px}
  .module{margin-bottom:18px}
  .module h2{display:flex;align-items:flex-start;gap:8px;font-family:"Oswald",sans-serif;font-weight:500;font-size:18px;color:var(--green-dark);text-transform:uppercase;line-height:1.2;margin-bottom:5px}
  .module h2 .tick{margin-top:3px}
  .module p{font-size:12.5px;line-height:1.5;padding-left:24px}

  .reviews{position:absolute;left:480px;top:858px;width:390px;border-top:2px solid var(--green);padding-top:10px}
  .reviews h3{font-family:"Oswald",sans-serif;font-weight:500;font-size:18px;color:var(--blue);text-transform:uppercase;margin-bottom:6px}
  .review{font-style:italic;font-size:13px;line-height:1.45;color:var(--navy);padding:5px 0 5px 12px;border-left:3px solid var(--green);margin-bottom:6px}

  .footer{position:absolute;left:0;bottom:0;width:900px;height:140px;background:var(--navy)}
  .footer-accent{position:absolute;left:0;top:0;width:900px;height:8px;background:var(--green)}
  .contact{position:absolute;left:40px;top:40px;color:#fff}
  .contact .phone{font-size:22px;font-weight:700}
  .contact .address{font-size:14px;margin-top:6px;opacity:.9}
  .web{position:absolute;right:40px;top:60px;color:var(--green);font-size:18px;font-weight:600}
</style>
</head>
<body>
  <div class="hero-photo" role="img" aria-label="Photo of a tall glass office building against the sky"></div>
  <svg class="hero-band" viewBox="0 0 900 360" aria-hidden="true">
    <polygon points="343,360 360,360 450,0 433,0" fill="#5aa832"/>
  </svg>

  <div class="brand">
    <span class="brand-dot"></span>
    <span class="brand-name">Northgate Trade Compliance</span>
  </div>

  <div class="title">
    <h1>Module<br><span class="accent">Training</span></h1>
    <div class="subtitle">Half Day Training Sessions</div>
  </div>

  <table class="sessions">
    <tr><td class="pick"><input class="tick" type="checkbox" aria-label="Sydney"></td><td class="city">Sydney</td><td class="date">27 &amp; 28 April</td></tr>
    <tr><td class="pick"><input class="tick" type="checkbox" aria-label="Canberra"></td><td class="city">Canberra</td><td class="date">29 April (Module 1 &amp; 2 only)</td></tr>
    <tr><td class="pick"><input class="tick" type="checkbox" aria-label="Brisbane"></td><td class="city">Brisbane</td><td class="date">2 &amp; 3 May</td></tr>
  </table>

  <div class="price">PRICE: $495 <small>(INC GST)</small></div>

  <div class="team-photo" role="img" aria-label="Photo of a smiling business team in an office"></div>

  <section class="modules">
    <article class="module">
      <h2><input class="tick" type="checkbox" aria-label="Module 1"><span>1. Australian Export Controls and AU/US Trade Treaty</span></h2>
      <p>This half day module provides attendees with guidance on Australian Export Controls and the recent changes and provides guidance on management of the new requirements. Included in this session is information with regard to the Trade Co-operation Treaty.</p>
    </article>
    <article class="module">
      <h2><input class="tick" type="checkbox" aria-label="Module 2"><span>2. Jurisdiction/Classification</span></h2>
      <p>This half day module will take attendees through export control reforms and provide practical step by step guidance on Jurisdiction and Classification of U.S. controlled technology. Attendees will be encouraged to bring their own examples to be worked through during the training session.</p>
    </article>
    <article class="module">
      <h2><input class="tick" type="checkbox" aria-label="Module 3"><span>3. Dual Nationals, Discrimination and Privacy</span></h2>
      <p>The contradictions between the U.S. Dual National Requirements and Australian Anti-Discrimination law have been an issue for the Australian defence industry. Further compounding the issue is the new Australian Privacy Legislation. This module provides attendees with guidance on how to manage the issue and tips and hints on mitigation strategies.</p>
    </article>
    <article class="module">
      <h2><input class="tick" type="checkbox" aria-label="Module 4"><span>4. Exemptions, Exceptions &amp; De Minimis</span></h2>
      <p>Exemptions, Exceptions and De minimis primarily allow exporters to export U.S. controlled technology without prior approval; however, there are restrictions. This module will explore Exemptions, Exceptions and De minimis and provide practical guidance on implementation and management.</p>
    </article>
  </section>

  <section class="reviews">
    <h3>What past attendees say</h3>
    <p class="review">“Great training, best I've ever had on this topic.”</p>
    <p class="review">“Great presenter - very knowledgable.”</p>
    <p class="review">“Course was very well presented and organised.”</p>
  </section>

  <footer class="footer">
    <div class="footer-accent"></div>
    <div class="contact">
      <div class="phone">Phone: 61 (0)7 5550 1234</div>
      <div class="address">Level 2, 14 Harbour Lane, Seaview</div>
    </div>
    <div class="web">http://tradecomply-training.example/</div>
  </footer>
</body>
</html>
```